Boutique custom software development company needs new business card

Our nearly 20 year old custom software development company would like to better include the fact that we are now providing Bitcoin services. These new services are B2B include education (how to acquire and securely hold Bitcoin) and integrating Bitcoin payments into existing ecommerce sites or other existing systems. Please keep the card clean and simple. Attached is our current design and some other files. vexalon.example

Target Market(s)

businesses owners interested in long term relationship

Industry/Entity Type

Custom software development and Bitcoin

Contact Information for Business Card

Marcus Ellwood, marcus@vexalon.example, vexalon.example, (888) 555-VEXAL

Font styles to use
Other font styles liked:
• monospace

Requirements
Must have
• double-sided
Nice to have
• clean and simple
Should not have
• physical address

```html
<!DOCTYPE html>
<html lang="en">
<head>
<meta charset="utf-8">
<title>Vexalon business card</title>
<link rel="stylesheet" href="https://fonts.googleapis.com/css2?family=Montserrat:wght@400;700;800&family=Arimo:wght@400;700&display=swap">
<style>
  :root {
    --bg: #e4e4e2;
    --card-white: #ffffff;
    --brand-blue: #3d6fb8;
    --brand-orange: #f07822;
    --edge-orange: #d9601a;
    --rule-grey: #8a8a8a;
    --text-grey: #5a5a5a;
    --back-mark: #f9a469;
  }
  * { box-sizing: border-box; margin: 0; padding: 0; }
  html, body { width: 1200px; height: 801px; overflow: hidden; }
  body {
    background: var(--bg);
    position: relative;
    font-family: "Arimo", Arial, sans-serif;
  }
  .card {
    position: absolute;
    top: 246px;
    width: 540px;
    height: 309px;
    border-bottom: 3px solid var(--edge-orange);
    overflow: hidden;
  }
  .card-front { left: 40px; background: var(--card-white); }
  .card-back { left: 620px; background: var(--brand-orange); }

  .wordmark {
    position: absolute;
    right: 62px;
    top: 52px;
  }
  .wordmark-name {
    font-family: "Montserrat", sans-serif;
    font-weight: 800;
    font-size: 50px;
    letter-spacing: 1px;
    color: var(--brand-blue);
    line-height: 1;
  }
  .wordmark-tagline {
    font-family: "Montserrat", sans-serif;
    font-weight: 400;
    font-size: 15.5px;
    color: var(--brand-blue);
    margin-top: 4px;
    letter-spacing: -0.2px;
  }

  .person-name {
    position: absolute;
    left: 66px;
    top: 176px;
    font-weight: 700;
    font-size: 22px;
    letter-spacing: 0.5px;
  }
  .person-name .first { color: var(--brand-orange); }
  .person-name .last { color: var(--brand-blue); }

  .divider {
    position: absolute;
    left: 66px;
    right: 48px;
    top: 203px;
    height: 1px;
    background: var(--rule-grey);
  }

  .contact-list {
    position: absolute;
    left: 66px;
    top: 214px;
    list-style: none;
    color: var(--text-grey);
    font-size: 13.5px;
    line-height: 20px;
  }
  .contact-list li { display: flex; align-items: center; gap: 8px; }
  .contact-list svg { width: 12px; height: 12px; flex: none; }

  .services {
    position: absolute;
    right: 48px;
    top: 214px;
    width: 190px;
    list-style: none;
    color: var(--text-grey);
    font-size: 13.5px;
    line-height: 20px;
  }

  .back-name {
    position: absolute;
    inset: 0;
    display: flex;
    align-items: center;
    justify-content: center;
    font-family: "Montserrat", sans-serif;
    font-weight: 800;
    font-size: 54px;
    letter-spacing: 2px;
    color: var(--back-mark);
  }
</style>
</head>
<body>
  <section class="card card-front">
    <div class="wordmark">
      <div class="wordmark-name">VEXALON</div>
      <div class="wordmark-tagline">developer of custom applications</div>
    </div>

    <div class="person-name"><span class="first">MARCUS</span> <span class="last">ELLWOOD</span></div>
    <div class="divider"></div>

    <ul class="contact-list">
      <li>
        <svg viewBox="0 0 12 12" aria-hidden="true"><path d="M3 1 L5 3.5 L4 5 Q5.5 7.5 7 8 L8.5 7 L11 9 L9.5 11 Q4 10 1 3 Z" fill="var(--brand-orange)"/></svg>
        (888) 555-VEXAL
      </li>
      <li>
        <svg viewBox="0 0 12 12" aria-hidden="true"><rect x="1" y="2.5" width="10" height="7" fill="none" stroke="var(--brand-orange)" stroke-width="1.2"/><path d="M1 2.5 L6 6.5 L11 2.5" fill="none" stroke="var(--brand-orange)" stroke-width="1.2"/></svg>
        marcus@vexalon.example
      </li>
      <li>
        <svg viewBox="0 0 12 12" aria-hidden="true"><circle cx="6" cy="6" r="5" fill="none" stroke="var(--brand-orange)" stroke-width="1.2"/><ellipse cx="6" cy="6" rx="2.2" ry="5" fill="none" stroke="var(--brand-orange)" stroke-width="1"/><path d="M1 6 H11 M2 3.5 H10 M2 8.5 H10" stroke="var(--brand-orange)" stroke-width="0.9"/></svg>
        www.vexalon.example
      </li>
    </ul>

    <ul class="services">
      <li>custom software</li>
      <li>bitcoin education</li>
      <li>bitcoin payments</li>
    </ul>
  </section>

  <section class="card card-back">
    <div class="back-name">VEXALON</div>
  </section>
</body>
</html>
```